3" Round Business Card for Funeral Home

We need a business card designed for our cremation service. We would like to use a 3" round business card.

The business card will be 2-sided. One side with the logo featured prominently. The back sad will have employee name and contact info.

Templates for printing have been attached to project as well as logo

We like soft colors like the logo. Final design should promote a feeling of trust.

Industry/Entity Type

Funeral

Contact Information for Business Card

Employee Name, Phone number, email, web address

Requirements
Should not have
• any sort of funeral item such as urn, casket, hearse, tombstone

```html
<!DOCTYPE html>
<html lang="en">
<head>
<meta charset="utf-8">
<title>Round Business Card – Front and Back</title>
<link rel="stylesheet" href="https://fonts.googleapis.com/css2?family=Fondamento&display=swap">
<style>
  :root {
    --backdrop: #2b2b2b;
    --paper: #ffffff;
    --teal: #1baaa0;
    --plum: #8b2a8c;
    --ink-grey: #7a7a7a;
  }
  html, body {
    margin: 0;
    padding: 0;
    overflow: hidden;
    background: var(--backdrop);
  }
  .canvas {
    display: block;
    width: 1200px;
    height: 582px;
  }
  .card-paper { fill: var(--paper); }
  .card-band { fill: var(--teal); }
  .card-ring { fill: none; stroke: var(--teal); stroke-width: 1; }
  .brand-name {
    font-family: "Fondamento", serif;
    font-size: 40px;
    fill: var(--teal);
  }
  .holder-name {
    font-family: "Fondamento", serif;
    font-size: 38px;
    fill: var(--teal);
  }
  .holder-title {
    font-family: "Fondamento", serif;
    font-size: 20px;
    fill: var(--plum);
  }
  .contact-line {
    font-family: "Fondamento", serif;
    font-size: 14px;
    fill: var(--ink-grey);
  }
  .contact-icon-dot { fill: var(--plum); }
  .contact-icon-glyph { fill: var(--paper); }
</style>
</head>
<body>
<svg class="canvas" viewBox="0 0 1200 582" xmlns="http://www.w3.org/2000/svg">
  <defs>
    <clipPath id="front-disc"><circle cx="348" cy="291" r="212"/></clipPath>
    <clipPath id="back-disc"><circle cx="827" cy="291" r="212"/></clipPath>
  </defs>

  <!-- Front: brand side -->
  <g class="card card-front">
    <circle class="card-paper" cx="348" cy="291" r="212"/>
    <circle class="card-ring" cx="348" cy="291" r="188"/>
    <g clip-path="url(#front-disc)">
      <rect class="card-band" x="130" y="291" width="440" height="230"/>
    </g>
    <path class="card-paper" d="M198 291 H498 V323 Q498 332 489 332 H207 Q198 332 198 323 Z"/>
    <text class="brand-name" x="348" y="300" text-anchor="middle">gentleRest.com</text>
  </g>

  <!-- Back: contact side -->
  <g class="card card-back">
    <circle class="card-paper" cx="827" cy="291" r="212"/>
    <circle class="card-ring" cx="827" cy="291" r="188"/>
    <g clip-path="url(#back-disc)">
      <rect class="card-band" x="610" y="70" width="440" height="157"/>
    </g>
    <path class="card-paper" d="M742 227 V190 Q742 181 751 181 H900 Q909 181 909 190 V227 Z"/>
    <text class="holder-name" x="826" y="218" text-anchor="middle">John Doe</text>
    <text class="holder-title" x="826" y="247" text-anchor="middle">Mangaer</text>

    <g class="contact-item">
      <circle class="contact-icon-dot" cx="826" cy="273" r="6"/>
      <path class="contact-icon-glyph" d="M823.2 270.2 l1.4-0.6 1 2 -0.9 0.7 q0.6 1.3 1.9 1.9 l0.7-0.9 2 1 -0.6 1.4 q-3.3 0.2 -5.5-5.5z"/>
      <text class="contact-line" x="826" y="293" text-anchor="middle">111-222-333</text>
    </g>
    <g class="contact-item">
      <circle class="contact-icon-dot" cx="826" cy="309" r="6"/>
      <rect class="contact-icon-glyph" x="822.5" y="306.5" width="7" height="5" rx="0.6"/>
      <path d="M822.8 307 L826 309.6 L829.2 307" fill="none" stroke="var(--plum)" stroke-width="0.8"/>
      <text class="contact-line" x="826" y="328" text-anchor="middle">info@quietwillow.com</text>
    </g>
    <g class="contact-item">
      <circle class="contact-icon-dot" cx="826" cy="345" r="6"/>
      <path class="contact-icon-glyph" d="M826 341.5 L829.5 344.6 H828.5 V348 H823.5 V344.6 H822.5 Z"/>
      <text class="contact-line" x="826" y="364" text-anchor="middle">your address,your city,box 88900</text>
    </g>
  </g>
</svg>
</body>
</html>
```